Brookside Grocer

Hope all is well!

Wanted to make business cards for my father. His name is Faisal Qureshi and owns convenience stores. I have attached logo :)

He does not want any title just simple name and phone. An email would be nice as well.

Faisal Qureshi
Cell: 413-585-2046
Store: 413-719-4820

Brooksidegrocer512@fernpost.com

The design and style is totally up to you :) The colors we were looking for were the same as logo :)

```html
<!DOCTYPE html>
<html lang="en">
<head>
<meta charset="utf-8">
<title>Brookside Grocer — Business Card</title>
<link rel="stylesheet" href="https://fonts.googleapis.com/css2?family=Open+Sans:wght@400;800&display=swap">
<style>
  :root {
    --backdrop: #c9c9c9;
    --brand-red: #ea343a;
    --brand-navy: #1f3a7a;
    --card-white: #ffffff;
    --ink: #1a1a1a;
    --card-shadow: 0 18px 30px rgba(0,0,0,.28);
  }
  * { box-sizing: border-box; margin: 0; padding: 0; }
  html, body {
    width: 1200px; height: 900px; overflow: hidden;
    background: var(--backdrop);
    font-family: "Open Sans", Arial, sans-serif;
  }
  .stage {
    width: 1200px; height: 900px;
    display: flex; flex-direction: column; align-items: center; justify-content: center;
    gap: 44px;
  }
  .card {
    width: 700px; height: 400px;
    border-radius: 34px;
    box-shadow: var(--card-shadow);
    position: relative;
    overflow: hidden;
  }
  .card--front {
    background: var(--brand-red);
    display: flex; align-items: center; justify-content: center;
  }
  .wordmark {
    display: flex; align-items: center; gap: 18px;
    font-weight: 800;
    white-space: nowrap;
  }
  .wordmark__dot {
    border-radius: 50%;
    flex: none;
  }
  .card--front .wordmark { color: var(--card-white); font-size: 54px; }
  .card--front .wordmark__dot { width: 34px; height: 34px; background: var(--card-white); }

  .card--back {
    background: var(--card-white);
    display: grid;
    grid-template-columns: 330px 2px 1fr;
    align-items: center;
  }
  .card--back .wordmark {
    justify-self: center;
    color: var(--brand-navy); font-size: 30px; gap: 10px;
  }
  .card--back .wordmark__dot { width: 18px; height: 18px; background: var(--brand-red); }
  .divider {
    width: 2px; height: 200px;
    background: var(--brand-red);
  }
  .contact { padding-left: 34px; }
  .contact__name {
    font-weight: 800; font-size: 28px; color: var(--brand-navy);
    margin-bottom: 40px;
  }
  .contact__surname { color: var(--brand-red); }
  .contact__list { list-style: none; }
  .contact__item {
    display: flex; align-items: center; gap: 10px;
    font-size: 15px; color: var(--ink); line-height: 1.6;
  }
  .contact__icon { width: 14px; height: 14px; flex: none; fill: var(--brand-red); }
</style>
</head>
<body>
<main class="stage">
  <section class="card card--front" aria-label="Card front">
    <div class="wordmark"><span class="wordmark__dot"></span>Brookside Grocer</div>
  </section>

  <section class="card card--back" aria-label="Card back">
    <div class="wordmark"><span class="wordmark__dot"></span>Brookside Grocer</div>
    <div class="divider"></div>
    <div class="contact">
      <h1 class="contact__name">Faisal <span class="contact__surname">Qureshi</span></h1>
      <ul class="contact__list">
        <li class="contact__item">
          <svg class="contact__icon" viewBox="0 0 14 14" aria-hidden="true"><path d="M4 0h6a1.5 1.5 0 0 1 1.5 1.5v11A1.5 1.5 0 0 1 10 14H4a1.5 1.5 0 0 1-1.5-1.5v-11A1.5 1.5 0 0 1 4 0zm0 2v9h6V2zm3 9.6a.8.8 0 1 0 0 1.6.8.8 0 0 0 0-1.6z"/></svg>
          413-585-2046 (Cell)
        </li>
        <li class="contact__item">
          <svg class="contact__icon" viewBox="0 0 14 14" aria-hidden="true"><path d="M3 1l2.2 2.6-1.1 1.6a8 8 0 0 0 4.7 4.7l1.6-1.1L13 11l-1.4 2A11.5 11.5 0 0 1 1 2.4z"/></svg>
          413-719-4820 (Store)
        </li>
        <li class="contact__item">
          <svg class="contact__icon" viewBox="0 0 14 14" aria-hidden="true"><path d="M0 3h14v1L7 8.2 0 4zm0 2.4l7 4.2 7-4.2V12H0z"/></svg>
          Brooksidegrocer512@fernpost.com
        </li>
      </ul>
    </div>
  </section>
</main>
</body>
</html>
```